Brightlane Photography
Sports & Dance Photography
Brightlane Photography - Photography
Creative Brief
Photography
Sports Leagues and Dance Schools
I have included an old brocure for sme reference material on our services. I would like trifold format
Marcotoledo Marcotoledo
Please download the asset file

```html
<!DOCTYPE html>
<html lang="en">
<head>
<meta charset="utf-8">
<title>Brightlane Photography – Trifold Brochure</title>
<link href="https://fonts.googleapis.com/css2?family=Poppins:wght@400;500;600;700;800&display=swap" rel="stylesheet">
<style>
  :root {
    --stage: #dcdcdc;
    --navy: #14202b;
    --navy-deep: #0d161e;
    --coral: #f0533f;
    --coral-light: #f4715e;
    --pink: #ec2b7a;
    --teal: #4cc4b8;
    --lime: #b5e61d;
    --white: #ffffff;
    --ink: #3a3a3a;
    --muted: #8e96a0;
  }
  * { box-sizing: border-box; margin: 0; padding: 0; }
  html, body { width: 1200px; height: 799px; overflow: hidden; }
  body {
    background: var(--stage);
    font-family: "Poppins", Arial, sans-serif;
    position: relative;
  }
  .brochure {
    position: absolute;
    left: 90px; top: 50px;
    width: 1020px; height: 700px;
    display: flex;
    box-shadow: 0 18px 40px rgba(0,0,0,0.18);
  }
  .panel { position: relative; width: 340px; height: 100%; overflow: hidden; }

  /* Left panel */
  .panel--back { background: var(--navy); }
  .photo-athlete {
    position: absolute; left: 0; top: 0; width: 100%; height: 440px;
    background: radial-gradient(ellipse at 55% 45%, #6b4a3a 0%, #3a2b26 35%, var(--navy-deep) 80%);
  }
  .brand {
    display: flex; align-items: center; gap: 8px;
  }
  .brand__mark { width: 14px; height: 14px; border-radius: 50%; background: var(--lime); }
  .brand__name { font-weight: 800; font-size: 24px; color: var(--white); letter-spacing: 0.5px; }
  .brand__tagline { font-size: 9px; letter-spacing: 2px; color: var(--white); text-transform: uppercase; margin-top: 2px; }
  .panel--back .brand-block { position: absolute; left: 36px; top: 480px; }
  .contact { position: absolute; left: 36px; top: 580px; font-size: 11px; line-height: 1.7; color: var(--white); }

  /* Middle panel */
  .panel--inner { background: var(--white); }
  .coral-top { position: absolute; left: 0; top: 0; width: 100%; height: 260px; }
  .headline-small {
    position: absolute; left: 0; right: 0; top: 46px;
    text-align: center; color: var(--white); line-height: 1.15;
  }
  .headline-small .line-light { font-size: 17px; font-weight: 400; }
  .headline-small .line-bold { font-size: 22px; font-weight: 700; text-transform: uppercase; }
  .admin-button {
    position: absolute; left: 50%; top: 278px; transform: translateX(-50%);
    background: var(--pink); color: var(--white);
    font-size: 13px; font-weight: 600; letter-spacing: 1px;
    padding: 6px 22px; border-radius: 4px;
  }
  .admin-copy {
    position: absolute; left: 40px; right: 40px; top: 320px;
    font-size: 9.5px; line-height: 1.5; color: var(--ink); text-align: center;
  }
  .teal-circle {
    position: absolute; left: 50%; top: 470px; transform: translateX(-50%);
    width: 300px; height: 300px; border-radius: 50%; background: var(--teal);
  }
  .photo-dancers {
    position: absolute; left: 70px; top: 395px; width: 200px; height: 250px;
    border-radius: 6px;
    background: linear-gradient(180deg, #d9c7c0 0%, #4a3f44 55%, #1d1a1f 100%);
  }

  /* Right panel */
  .panel--cover { background: var(--navy); }
  .panel--cover .brand-block { position: absolute; left: 0; right: 0; top: 50px; display: flex; flex-direction: column; align-items: center; }
  .cover-title { position: absolute; left: 34px; top: 150px; color: var(--white); text-transform: uppercase; }
  .cover-title__lead { font-size: 20px; font-weight: 500; }
  .cover-title__main { font-size: 52px; font-weight: 800; line-height: 0.98; color: var(--lime); }
  .cover-title__tail { font-size: 18px; font-weight: 600; margin-top: 6px; }
  .photo-football {
    position: absolute; left: 0; bottom: 0; width: 100%; height: 330px;
    background: radial-gradient(ellipse at 50% 55%, #3a3f46 0%, #1c232b 50%, var(--navy) 85%);
  }
</style>
</head>
<body>
  <main class="brochure">
    <section class="panel panel--back">
      <div class="photo-athlete" role="img" aria-label="Photo of a female basketball player holding a ball against a dark background"></div>
      <div class="brand-block">
        <div class="brand"><span class="brand__mark"></span><span class="brand__name">BRIGHTLANE</span></div>
        <div class="brand__tagline">Sports Photography</div>
      </div>
      <div class="contact">
        <p>info@brightlanephoto.ca</p>
        <p>www.brightlanephoto.ca</p>
      </div>
    </section>

    <section class="panel panel--inner">
      <svg class="coral-top" viewBox="0 0 340 260" preserveAspectRatio="none" aria-hidden="true">
        <path d="M0 0 H340 V200 Q170 280 0 230 Z" fill="var(--coral)"/>
      </svg>
      <div class="headline-small">
        <p class="line-light">Ever needed an answer or</p>
        <p class="line-bold">Needed a</p>
        <p class="line-bold">Shipping Update</p>
        <p class="line-light">Information &amp; power</p>
      </div>
      <div class="admin-button">ADMIN ACCESS</div>
      <p class="admin-copy">Log in to see every gallery, track your print orders and get quick answers from our team. Your photos, your orders and your updates, all in one simple place.</p>
      <div class="teal-circle"></div>
      <div class="photo-dancers" role="img" aria-label="Photo of a group of dancers posing together"></div>
    </section>

    <section class="panel panel--cover">
      <div class="brand-block">
        <div class="brand"><span class="brand__mark"></span><span class="brand__name">BRIGHTLANE</span></div>
        <div class="brand__tagline">Sports Photography</div>
      </div>
      <div class="cover-title">
        <p class="cover-title__lead">The pathway to</p>
        <p class="cover-title__main">Easier &amp;<br>Better</p>
        <p class="cover-title__tail">Sports photos is here...</p>
      </div>
      <div class="photo-football" role="img" aria-label="Photo of an American football player in helmet holding a football"></div>
    </section>
  </main>
</body>
</html>
```